Business Cards for a law firm

Business cards for our law firm. Use our silhoette logo and OAK COUNSEL - check our website (www.oakcounsel.com)

Contact Information for Business Card

our silhouette logo, OAK COUNSEL, 800-555-0147, Dariel Montague, dariel@oakcounsel.com

Requirements
Must have
• our silhouette logo, OAK COUNSEL, 800-555-0147, Dariel Montague, dariel@oakcounsel.com

```html
<!DOCTYPE html>
<html lang="en">
<head>
<meta charset="utf-8">
<title>Oak Counsel – Business Cards</title>
<link rel="stylesheet" href="https://fonts.googleapis.com/css2?family=Lexend+Exa:wght@300&family=Montserrat:wght@400;700&display=swap">
<style>
  :root {
    --backdrop: #2a2a2b;
    --card: #ffffff;
    --navy: #1f2c6b;
    --ink: #1c1c22;
  }
  * { margin: 0; padding: 0; box-sizing: border-box; }
  html, body {
    width: 1200px;
    height: 900px;
    overflow: hidden;
    background: var(--backdrop);
  }
  .canvas {
    position: relative;
    width: 1200px;
    height: 900px;
  }
  .card {
    position: absolute;
    left: 250px;
    width: 700px;
    height: 400px;
    background: var(--card);
    border-radius: 26px;
    overflow: hidden;
  }
  .card--front { top: 40px; }
  .card--back  { top: 460px; }

  .brand {
    position: absolute;
    display: flex;
    align-items: center;
    gap: 18px;
  }
  .brand__mark {
    width: 46px;
    height: 46px;
    background: var(--navy);
  }
  .brand__name {
    font-family: "Lexend Exa", sans-serif;
    font-weight: 300;
    color: var(--navy);
    letter-spacing: 1px;
    white-space: nowrap;
  }
  .card--front .brand { left: 62px; top: 108px; }
  .card--front .brand__name { font-size: 40px; }

  .card--back .brand {
    left: 50%;
    top: 50%;
    transform: translate(-50%, -50%);
  }
  .card--back .brand__name { font-size: 40px; }

  .divider {
    position: absolute;
    left: 120px;
    right: 48px;
    top: 214px;
    height: 2px;
    background: var(--navy);
  }

  .person {
    position: absolute;
    left: 100px;
    top: 232px;
    font-family: "Montserrat", sans-serif;
  }
  .person__name {
    font-size: 27px;
    font-weight: 700;
    color: var(--navy);
    line-height: 1.1;
  }
  .person__role {
    font-size: 15px;
    font-weight: 400;
    color: var(--ink);
    margin-top: 2px;
  }

  .contact {
    position: absolute;
    left: 104px;
    top: 304px;
    list-style: none;
    font-family: "Montserrat", sans-serif;
    font-size: 15px;
    color: var(--ink);
  }
  .contact__item {
    display: flex;
    align-items: center;
    gap: 10px;
    line-height: 24px;
  }
  .contact__icon {
    width: 13px;
    height: 13px;
    fill: var(--navy);
    flex: none;
  }
</style>
</head>
<body>
<main class="canvas">

  <section class="card card--front" aria-label="Business card front">
    <div class="brand">
      <span class="brand__mark"></span>
      <span class="brand__name">OAK COUNSEL</span>
    </div>

    <div class="divider"></div>

    <div class="person">
      <p class="person__name">Dariel Montague</p>
      <p class="person__role">Attorney at Law</p>
    </div>

    <ul class="contact">
      <li class="contact__item">
        <svg class="contact__icon" viewBox="0 0 16 16" aria-hidden="true">
          <path d="M1 5c0-2 3-3 7-3s7 1 7 3v2h-4V5.5C10 5 6 5 5 5.5V7H1z"/>
          <path d="M3 8h10l1 6H2z"/>
        </svg>
        <span>800-555-0147</span>
      </li>
      <li class="contact__item">
        <svg class="contact__icon" viewBox="0 0 16 16" aria-hidden="true">
          <path d="M1 3h14v1.5L8 9 1 4.5z"/>
          <path d="M1 6.2l7 4.5 7-4.5V13H1z"/>
        </svg>
        <span>dariel@oakcounsel.com</span>
      </li>
      <li class="contact__item">
        <svg class="contact__icon" viewBox="0 0 16 16" aria-hidden="true">
          <circle cx="8" cy="8" r="7"/>
          <path d="M1 8h14M8 1c-3 3-3 11 0 14M8 1c3 3 3 11 0 14" stroke="#fff" stroke-width="1" fill="none"/>
        </svg>
        <span>www.oakcounsel.com</span>
      </li>
    </ul>
  </section>

  <section class="card card--back" aria-label="Business card back">
    <div class="brand">
      <span class="brand__mark"></span>
      <span class="brand__name">OAK COUNSEL</span>
    </div>
  </section>

</main>
</body>
</html>
```